Company business card

We need a new business card design. We are IT company which is specialized for outsourcing of operations hardware and software (specially Velbrandt, we are a partner), developing custom applications and web applications, BPM solutions, auditing hw and sw. actually design was attached. But we need completely NEW.

Industry/Entity Type

Business

```html
<!DOCTYPE html>
<html lang="en">
<head>
<meta charset="utf-8">
<title>KELVARA business card</title>
<link rel="stylesheet" href="https://fonts.googleapis.com/css2?family=Montserrat:wght@500;600;700&family=Source+Sans+3:wght@400&display=swap">
<style>
  :root {
    --backdrop: #a9a7a8;
    --brand-blue: #3566a8;
    --brand-blue-dark: #2e5b98;
    --paper: #fbfbfb;
    --stripe-grey: #8a8a8c;
    --white: #ffffff;
  }
  * { margin: 0; padding: 0; box-sizing: border-box; }
  html, body {
    width: 1200px; height: 1200px; overflow: hidden;
    background: var(--backdrop);
  }
  .card {
    position: absolute;
    border-radius: 24px;
    overflow: hidden;
  }
  .card-front {
    left: 238px; top: 117px; width: 714px; height: 420px;
    background: linear-gradient(160deg, var(--brand-blue) 0%, var(--brand-blue-dark) 100%);
  }
  .card-back {
    left: 230px; top: 645px; width: 712px; height: 417px;
    background: var(--paper);
    color: var(--brand-blue);
  }
  .front-texture {
    position: absolute; inset: 0;
    background: radial-gradient(ellipse at 50% 40%, rgba(255,255,255,0.06), rgba(255,255,255,0) 70%);
  }
  .brand-name {
    position: absolute;
    font-family: "Montserrat", sans-serif;
    font-weight: 700;
    line-height: 1;
    letter-spacing: 2px;
    white-space: nowrap;
  }
  .card-front .brand-name {
    left: 0; right: 0; top: 168px;
    text-align: center;
    font-size: 84px; color: var(--white);
  }
  .card-back .brand-name {
    left: 46px; top: 92px;
    font-size: 54px; color: var(--brand-blue);
  }
  .person { position: absolute; left: 408px; top: 110px; }
  .person-name {
    font-family: "Montserrat", sans-serif; font-weight: 600;
    font-size: 27px; letter-spacing: 0.5px;
  }
  .person-role {
    font-family: "Source Sans 3", sans-serif; font-size: 16px;
    margin-top: 8px; letter-spacing: 0.5px;
  }
  .company { position: absolute; left: 46px; top: 262px; }
  .company-name {
    font-family: "Montserrat", sans-serif; font-weight: 600;
    font-size: 27px; letter-spacing: 0.5px;
  }
  .company-address {
    font-family: "Source Sans 3", sans-serif; font-size: 17px;
    line-height: 23px; margin-top: 10px;
  }
  .contacts {
    position: absolute; left: 406px; top: 271px; list-style: none;
    font-family: "Source Sans 3", sans-serif; font-size: 18px;
  }
  .contacts li { display: flex; align-items: center; height: 27px; gap: 18px; }
  .contacts svg { width: 18px; height: 16px; fill: var(--brand-blue); flex: none; }
  .bottom-band { position: absolute; left: 0; bottom: 0; width: 712px; height: 30px; }
</style>
</head>
<body>

<section class="card card-front" aria-label="Card front">
  <div class="front-texture" role="img" aria-label="Faint background texture in lighter blue"></div>
  <div class="brand-name">KELVARA</div>
</section>

<section class="card card-back" aria-label="Card back">
  <div class="brand-name">KELVARA</div>

  <div class="person">
    <p class="person-name">Lukáš Brezina</p>
    <p class="person-role">CEO</p>
  </div>

  <div class="company">
    <p class="company-name">KELVARA s.r.o.</p>
    <p class="company-address">Lipová 12<br>821 04 Bratislava</p>
  </div>

  <ul class="contacts">
    <li>
      <svg viewBox="0 0 18 16" aria-hidden="true"><path d="M1 5c0-2 3-3 8-3s8 1 8 3v1h-4V4.5H5V6H1z"/><path d="M4 7h10l2 7H2z"/><circle cx="9" cy="10.5" r="2" fill="#fbfbfb"/></svg>
      <span>+421 (0) 900 555 214</span>
    </li>
    <li>
      <svg viewBox="0 0 18 16" aria-hidden="true"><rect x="1" y="3" width="16" height="11"/><path d="M1.5 3.5l7.5 6 7.5-6" fill="none" stroke="#fbfbfb" stroke-width="1.4"/></svg>
      <span>lukas.brezina@kelvara.sk</span>
    </li>
    <li>
      <svg viewBox="0 0 18 16" aria-hidden="true"><circle cx="9" cy="8" r="7"/><g fill="none" stroke="#fbfbfb" stroke-width="1"><ellipse cx="9" cy="8" rx="3" ry="7"/><path d="M2 8h14M3 4.5h12M3 11.5h12"/></g></svg>
      <span>www.kelvara.sk</span>
    </li>
  </ul>

  <svg class="bottom-band" viewBox="0 0 712 30" aria-hidden="true">
    <polygon points="0,2 240,2 298,30 0,30" fill="var(--brand-blue)"/>
    <polygon points="268,12 712,12 712,30 298,30" fill="var(--stripe-grey)"/>
    <polygon points="240,2 250,2 306,30 298,30" fill="#ffffff"/>
  </svg>
</section>

</body>
</html>
```